CAMPO DORMIDO

Campo Dormido is a tribute to the hidden treasures of Chile’s majestic mountain landscapes. Each bottle captures the essence of the Andes, where rugged peaks and fertile valleys create the perfect harmony for winemaking. With a label inspired by the mystique of the mountains, Campo Dormido invites you to uncover the rich flavors and stories hidden within its depths—a wine as bold and timeless as the land it comes from. the current design is old and not attractiv at all we want something new

Please create a mysterious, enigmatic label based on the typography and logo attached to the project. We need at least, at the entry level, five varietal products such as Carménère, Cabernet Sauvignon, Merlot, Chardonnay, and Malbec. Later, we would like to add more premium products, like a Reserva, a Special Reserva, or a Limited Edition. The design should be flexible and easily adaptable to accommodate various products while maintaining the same overall aesthetic.

Project Brief – Large-Scale Brand Label Design
We are developing a new large-scale brand with a structured range of wines. Below are the key design elements and specifications for the labels:

Entry-Level Wines (Bordeaux Bottle Shape)
Varietals: Cabernet Sauvignon, Carménère, Merlot, Cabernet-Merlot, Sauvignon Blanc.
Do not mention the word "varietals" on the label.
Next Level – Special Reserve (Burgundy Bottle Shape)
Varietals: Pinot Noir, Chardonnay, Syrah.
The label must include the mention "Special Reserve."
Premium Level – Limited (Heavy Conical Bottle Shape)
Varietal: Carménère-Malbec.
The label must include the mention "Limited."
Top Level – Secret Blend (Heavy Conical Bottle Shape)
Name on the label: "Secret Blend."
General Label Guidelines
Year: Only mention "2024" (do not include the word “vintage”).
Capsules: Use standard-colored capsules only (no branding).
Design Concept: The style should align with our brand identity. Please refer to www.malvorin-vins.example for inspiration and coherence.

Target Market(s)

younger generation,

Industry/Entity Type

Wines producer

Requirements
Must have
• the original logo with the name it is register We need to indicate the varietals Cabernet Sauvignon, the vintage 2024, the region DO Central Valley
Nice to have
• one white wines version of the label on a burgendy bottle shape and one red wines label on bordeau bottles sahpe

```html
<!DOCTYPE html>
<html lang="en">
<head>
<meta charset="utf-8">
<title>Campo Dormido – Carmenere Special Reserve Label</title>
<link rel="stylesheet" href="https://fonts.googleapis.com/css2?family=Cinzel:wght@400&family=Cormorant+Garamond:wght@500&family=Allura&display=swap">
<style>
  :root {
    --backdrop: #e4e4e4;
    --label-ink: #252323;
    --forest-dark: #1d1d1d;
    --forest-shadow: #3a362e;
    --gold-light: #f3dc97;
    --gold-mid: #c9a657;
    --gold-deep: #7a5a2c;
    --white: #f6f4ef;
  }
  * { margin: 0; padding: 0; box-sizing: border-box; }
  html, body {
    width: 1200px;
    height: 924px;
    overflow: hidden;
    background: var(--backdrop);
  }
  .label {
    position: absolute;
    left: 296px;
    top: 62px;
    width: 607px;
    height: 800px;
    background: var(--label-ink);
    overflow: hidden;
    box-shadow: 0 14px 30px rgba(0,0,0,0.25);
  }
  .forest-scene {
    position: absolute;
    left: 0; top: 0;
    width: 100%;
    height: 306px;
    background:
      linear-gradient(90deg, rgba(29,29,29,0.35) 0%, rgba(29,29,29,0) 20%, rgba(29,29,29,0.3) 38%, rgba(29,29,29,0) 55%, rgba(29,29,29,0.35) 72%, rgba(29,29,29,0) 88%),
      linear-gradient(180deg,
        var(--forest-dark) 0%,
        var(--forest-dark) 44%,
        var(--forest-shadow) 50%,
        #b8a06a 56%,
        var(--gold-light) 66%,
        var(--gold-light) 76%,
        var(--gold-mid) 88%,
        var(--gold-deep) 100%);
  }
  .wood-grain {
    position: absolute;
    left: 0; top: 306px;
    width: 100%;
    height: 384px;
    background: radial-gradient(ellipse at 30% 40%, #2c2a2a 0%, var(--label-ink) 70%);
  }
  .brand-mark {
    position: absolute;
    left: 289px;
    top: 356px;
    width: 28px;
    height: 28px;
    border-radius: 50%;
    background: var(--gold-mid);
  }
  .brand-name,
  .since,
  .varietal,
  .tier,
  .edition {
    position: absolute;
    left: 0;
    width: 100%;
    text-align: center;
    line-height: 1;
    font-weight: 400;
  }
  .brand-name {
    top: 400px;
    font-family: "Cinzel", serif;
    font-size: 22px;
    letter-spacing: 1px;
    color: var(--gold-mid);
  }
  .since {
    top: 428px;
    font-family: "Cormorant Garamond", serif;
    font-size: 8px;
    letter-spacing: 1.5px;
    color: var(--gold-mid);
  }
  .varietal {
    top: 492px;
    font-family: "Cinzel", serif;
    font-size: 50px;
    letter-spacing: 1px;
    color: var(--white);
  }
  .tier {
    top: 607px;
    font-family: "Allura", cursive;
    font-size: 38px;
    color: var(--gold-mid);
  }
  .edition {
    top: 650px;
    font-family: "Cinzel", serif;
    font-size: 13px;
    letter-spacing: 5px;
    color: var(--white);
  }
  .gold-flow {
    position: absolute;
    left: 0; bottom: 0;
    width: 100%;
    height: 110px;
    background: linear-gradient(176deg,
      var(--label-ink) 0%,
      #4a3a22 22%,
      var(--gold-mid) 40%,
      #2f2a25 55%,
      #8a6d3a 70%,
      var(--gold-light) 80%,
      #2a2622 100%);
  }
</style>
</head>
<body>
  <main class="label">
    <div class="forest-scene" role="img" aria-label="Mountain pine forest silhouette, dark treetops above a gold foil tree line"></div>
    <div class="wood-grain" role="img" aria-label="Subtle dark wood grain texture"></div>
    <span class="brand-mark" aria-hidden="true"></span>
    <p class="brand-name">CAMPO DORMIDO</p>
    <p class="since">SINCE 1880</p>
    <h1 class="varietal">CARMENERE</h1>
    <p class="tier">Special Reserve</p>
    <p class="edition">LIMITED EDITION</p>
    <div class="gold-flow" role="img" aria-label="Flowing gold foil wood grain band"></div>
  </main>
</body>
</html>
```